We need a logo for our business which is a dental clinic (i.e. dentistry).
We would lilke designs using the colour blue, green and black incorporating the words Corvasta Dental, possibly a smile or a tooth image can be considered for incorporation in the logo.

Industry/Entity Type

Dental

```html
<!DOCTYPE html>
<html lang="en">
<head>
<meta charset="utf-8">
<title>Corvasta Dental Clinic – Business Card</title>
<link rel="stylesheet" href="https://fonts.googleapis.com/css2?family=Montserrat:wght@300;400;700&display=swap">
<style>
  :root {
    --backdrop: #1d1d1f;
    --card-blue: #0a72d6;
    --card-blue-deep: #0866c4;
    --band-green: #00f26c;
    --band-blue: #0a6fd3;
    --rule-green: #2fe38a;
    --strip-light: #a9d3f7;
    --text-white: #ffffff;
    --text-dark: #0c1b33;
    --art-white: #f4f6f8;
  }
  * { box-sizing: border-box; margin: 0; padding: 0; }
  html, body {
    width: 1200px;
    height: 900px;
    overflow: hidden;
    background: var(--backdrop);
    font-family: "Montserrat", sans-serif;
  }
  .stage {
    width: 1200px;
    height: 900px;
    display: flex;
    align-items: center;
    justify-content: center;
  }
  .business-card {
    position: relative;
    width: 840px;
    height: 480px;
    background: var(--card-blue);
    overflow: hidden;
    box-shadow: 0 10px 30px rgba(0, 0, 0, 0.45);
  }
  .brand-band {
    position: absolute;
    left: 0;
    top: 118px;
    width: 100%;
    height: 156px;
    background: linear-gradient(90deg, var(--band-green) 0%, var(--band-green) 22%, #06b79a 52%, var(--band-blue) 82%);
    border-top: 1px solid var(--rule-green);
    border-bottom: 1px solid var(--rule-green);
    display: flex;
    align-items: center;
  }
  .tooth-mascot {
    position: absolute;
    left: 175px;
    top: 18px;
    width: 96px;
    height: 120px;
    border-radius: 42% 42% 30% 30%;
    background: var(--art-white);
  }
  .brand-name {
    position: absolute;
    left: 330px;
    top: 34px;
    color: var(--text-white);
    line-height: 1.15;
  }
  .brand-name .primary {
    display: block;
    font-weight: 700;
    font-size: 38px;
    letter-spacing: 2px;
  }
  .brand-name .secondary {
    display: block;
    font-weight: 300;
    font-size: 36px;
    letter-spacing: 1px;
  }
  .contact-strip {
    position: absolute;
    left: 0;
    top: 346px;
    width: 100%;
    height: 96px;
    background: linear-gradient(90deg, var(--card-blue-deep) 0%, #5fa9ee 35%, var(--strip-light) 55%, #5fa9ee 75%, var(--card-blue-deep) 100%);
    display: flex;
    justify-content: space-around;
    align-items: center;
    padding: 0 40px;
  }
  .contact-item {
    display: flex;
    flex-direction: column;
    align-items: center;
    gap: 10px;
    color: var(--text-dark);
    font-size: 17px;
    letter-spacing: 1.5px;
    font-weight: 400;
  }
  .contact-item svg {
    width: 30px;
    height: 30px;
  }
</style>
</head>
<body>
<main class="stage">
  <section class="business-card">
    <div class="brand-band">
      <div class="tooth-mascot" role="img" aria-label="Smiling cartoon tooth mascot illustration"></div>
      <h1 class="brand-name">
        <span class="primary">CORVASTA</span>
        <span class="secondary">DENTAL CLINIC</span>
      </h1>
    </div>
    <div class="contact-strip">
      <div class="contact-item">
        <svg viewBox="0 0 30 30" aria-hidden="true">
          <rect x="3" y="7" width="24" height="16" fill="none" stroke="#0c1b33" stroke-width="2"/>
          <polyline points="3,7 15,17 27,7" fill="none" stroke="#0c1b33" stroke-width="2"/>
        </svg>
        <span>CONTACT@EMAIL.COM</span>
      </div>
      <div class="contact-item">
        <svg viewBox="0 0 30 30" aria-hidden="true">
          <path d="M9 4 L13 9 L10.5 12 C12 16 14 18 18 19.5 L21 17 L26 21 L23 25 C14 25 5 16 5 7 Z" fill="#0c1b33"/>
        </svg>
        <span>123.567.890</span>
      </div>
      <div class="contact-item">
        <svg viewBox="0 0 30 30" aria-hidden="true">
          <g fill="none" stroke="#0c1b33" stroke-width="2">
            <circle cx="15" cy="15" r="11"/>
            <ellipse cx="15" cy="15" rx="5" ry="11"/>
            <line x1="4" y1="15" x2="26" y2="15"/>
            <line x1="6" y1="9" x2="24" y2="9"/>
            <line x1="6" y1="21" x2="24" y2="21"/>
          </g>
        </svg>
        <span>WWW.WEBSITE.COM</span>
      </div>
    </div>
  </section>
</main>
</body>
</html>
```